Packaging Design New Cosmetics Range

Small Establish online Beauty company is expanding it's product range into Serums, Sprays and Creams . We are looking for a new fresh packaging design for this launch.
We only use products that are Organic , Not Tested on Animals and Natural products
We would be interested in viewing a White Design , Black design and a designer choice of colors .
First Products are
Rose Water in 100ml glass bottle with box
and a set of 3 Face Serums Vit C , Retinol and Hyaluronic in 30ml Glass bottle = Box
Scrubs and creams will launch later in Q1 2020 however would like a similar feel across all products
Target Market(s)
SEA / US Markets
Industry/Entity Type
Cosmetics
Colors
Designer to choose colors to be used in the design.
Requirements
Must have
- Space Allocated for Product Use and Bar Codes on Box
Nice to have
- Organic , Not tested on animal Logo's

```html
<!DOCTYPE html>
<html lang="en">
<head>
<meta charset="utf-8">
<title>Lunea Rose Water Packaging</title>
<link rel="stylesheet" href="https://fonts.googleapis.com/css2?family=Oswald:wght@300;400&display=swap">
<style>
  :root {
    --page: #ffffff;
    --white-box: #f3f3f3;
    --white-side: #e6e6e6;
    --black-box: #3a3a3a;
    --black-side: #2e2e2e;
    --teal-box: #14a98b;
    --teal-side: #0f9479;
    --teal: #17a88a;
    --grey-text: #9b9b9b;
    --dark-text: #6f6f6f;
    --teal-text: #7fd6c3;
    --glass: #eef1f1;
    --glass-edge: #cfd5d5;
    --cap: #ddd6cc;
  }
  * { margin: 0; padding: 0; box-sizing: border-box; }
  html, body { width: 1200px; height: 622px; overflow: hidden; background: var(--page); }
  body { position: relative; font-family: "Oswald", sans-serif; font-weight: 300; }

  .box { position: absolute; top: 90px; height: 440px; display: flex; }
  .box--white { left: 40px; }
  .box--black { left: 335px; }
  .box--teal  { left: 630px; }

  .box__side { width: 70px; height: 100%; padding: 26px 7px 14px; display: flex; flex-direction: column; }
  .box__front { width: 210px; height: 100%; position: relative; display: flex; flex-direction: column; align-items: center; }

  .box--white .box__side { background: var(--white-side); color: var(--grey-text); }
  .box--white .box__front { background: var(--white-box); color: var(--grey-text); }
  .box--black .box__side { background: var(--black-side); color: var(--dark-text); }
  .box--black .box__front { background: var(--black-box); color: var(--dark-text); }
  .box--teal .box__side { background: var(--teal-side); color: var(--teal-text); }
  .box--teal .box__front { background: var(--teal-box); color: var(--teal-text); }

  .badge { width: 50px; height: 50px; border-radius: 50%; background: currentColor; opacity: .55; margin: 0 auto 16px; flex: none; }
  .usage { font-size: 5.5px; line-height: 1.6; letter-spacing: .2px; }
  .usage + .usage { margin-top: 5px; }
  .side-meta { margin-top: auto; }
  .side-meta__name { font-size: 8px; letter-spacing: 1.5px; margin-bottom: 4px; }
  .side-meta__row { display: flex; align-items: flex-start; gap: 4px; }
  .side-meta__size { font-size: 16px; font-weight: 400; line-height: 1; }
  .side-meta__origin { font-size: 6.5px; line-height: 1.2; }
  .barcode-space { height: 40px; margin-top: 8px; }

  .product-name { margin-top: 36px; font-size: 17px; letter-spacing: 4px; }
  .mark { margin-top: auto; width: 96px; height: 96px; border-radius: 50%; background: var(--teal); opacity: .85; }
  .box--teal .mark { background: #ffffff; opacity: .9; }
  .brand-name { margin-top: 6px; margin-bottom: 64px; font-size: 48px; line-height: 1.1; font-weight: 300; letter-spacing: 1px; color: var(--teal); }
  .box--teal .brand-name { color: #ffffff; }
  .front-footer { position: absolute; bottom: 18px; left: 18px; right: 18px; display: flex; justify-content: space-between; font-size: 10px; letter-spacing: 1.5px; }

  .bottle { position: absolute; left: 900px; top: 180px; width: 170px; height: 390px; }
  .bottle__cap { width: 52px; height: 92px; margin: 0 auto; background: var(--cap); border-radius: 3px 3px 0 0; }
  .bottle__neck { width: 70px; height: 10px; margin: 0 auto; background: var(--glass-edge); }
  .bottle__body { height: 290px; border: 3px solid var(--glass-edge); border-radius: 8px; background: linear-gradient(90deg, var(--glass) 0%, #ffffff 50%, var(--glass) 100%); display: flex; flex-direction: column; align-items: center; }
  .bottle__label { margin-top: 24px; font-size: 13px; letter-spacing: 3px; color: var(--dark-text); }
  .bottle__mark { margin-top: auto; width: 60px; height: 60px; border-radius: 50%; background: var(--teal); opacity: .85; }
  .bottle__brand { margin-top: 4px; margin-bottom: 36px; font-size: 38px; line-height: 1.1; color: var(--teal); }
</style>
</head>
<body>

  <section class="box box--white">
    <div class="box__side">
      <div class="badge"></div>
      <p class="usage">Mist lightly over clean skin morning and night. Shake well before use. Keep cool and away from direct light.</p>
      <p class="usage">Pure steam distilled rose petals with no added alcohol or colour. For external use only.</p>
      <div class="side-meta">
        <p class="side-meta__name">ROSE WATER</p>
        <div class="side-meta__row"><p class="side-meta__size">100ml</p><p class="side-meta__origin">Made<br>in USA</p></div>
        <div class="barcode-space"></div>
      </div>
    </div>
    <div class="box__front">
      <p class="product-name">ROSE WATER</p>
      <div class="mark"></div>
      <p class="brand-name">lunea</p>
      <div class="front-footer"><span>Made in USA</span><span>100ml</span></div>
    </div>
  </section>

  <section class="box box--black">
    <div class="box__side">
      <div class="badge"></div>
      <p class="usage">Mist lightly over clean skin morning and night. Shake well before use. Keep cool and away from direct light.</p>
      <p class="usage">Pure steam distilled rose petals with no added alcohol or colour. For external use only.</p>
      <div class="side-meta">
        <p class="side-meta__name">ROSE WATER</p>
        <div class="side-meta__row"><p class="side-meta__size">100ml</p><p class="side-meta__origin">Made<br>in USA</p></div>
        <div class="barcode-space"></div>
      </div>
    </div>
    <div class="box__front">
      <p class="product-name">ROSE WATER</p>
      <div class="mark"></div>
      <p class="brand-name">lunea</p>
      <div class="front-footer"><span>Made in USA</span><span>100ml</span></div>
    </div>
  </section>

  <section class="box box--teal">
    <div class="box__side">
      <div class="badge"></div>
      <p class="usage">Mist lightly over clean skin morning and night. Shake well before use. Keep cool and away from direct light.</p>
      <p class="usage">Pure steam distilled rose petals with no added alcohol or colour. For external use only.</p>
      <div class="side-meta">
        <p class="side-meta__name">ROSE WATER</p>
        <div class="side-meta__row"><p class="side-meta__size">100ml</p><p class="side-meta__origin">Made<br>in USA</p></div>
        <div class="barcode-space"></div>
      </div>
    </div>
    <div class="box__front">
      <p class="product-name">ROSE WATER</p>
      <div class="mark"></div>
      <p class="brand-name">lunea</p>
      <div class="front-footer"><span>Made in USA</span><span>100ml</span></div>
    </div>
  </section>

  <section class="bottle">
    <div class="bottle__cap"></div>
    <div class="bottle__neck"></div>
    <div class="bottle__body">
      <p class="bottle__label">ROSE WATER</p>
      <div class="bottle__mark"></div>
      <p class="bottle__brand">lunea</p>
    </div>
  </section>

</body>
</html>
```